New Business Card (to reflect updated website content and graphics)

I changed some text and graphics on my website, so I need a new business card.

Target Market(s)

Mostly women, ages 30 - 60.

Industry/Entity Type

Life Coaching

Contact Information for Business Card

Included in attached Word document

Font styles to use
Sans Serif

Requirements
Must have
• I am not a creative person, so I will defer to designer. Take a look at my website, and you can get a feel for me, my style, and my target audience. Thank You!

My 3 branding colors are included in attached Word document.

```html
<!DOCTYPE html>
<html lang="en">
<head>
<meta charset="utf-8">
<title>Bright Path Coaching – Business Card</title>
<link rel="stylesheet" href="https://fonts.googleapis.com/css2?family=Poppins:wght@300;400;500&family=Libre+Baskerville:wght@400&display=swap">
<style>
  :root {
    --teal: #2487a3;
    --teal-soft: #9fcbd8;
    --coral-soft: #f6c2b9;
    --paper: #ffffff;
    --ink: #4a4a4a;
    --stage: #2e2f31;
  }
  * { margin: 0; padding: 0; box-sizing: border-box; }
  html, body { width: 1200px; height: 900px; overflow: hidden; }
  body {
    background: var(--stage);
    font-family: "Poppins", sans-serif;
    position: relative;
  }
  .card {
    position: absolute;
    left: 250px;
    width: 700px;
    height: 400px;
    border-radius: 26px;
    overflow: hidden;
  }
  .card--front { top: 40px; background: var(--teal); color: var(--paper); }
  .card--back { top: 460px; background: var(--paper); color: var(--teal); }

  .brand {
    display: flex;
    flex-direction: column;
    align-items: center;
  }
  .brand__row { display: flex; align-items: center; gap: 12px; }
  .brand__dot {
    width: 20px; height: 20px; border-radius: 50%;
    border: 2px solid currentColor;
  }
  .brand__name {
    font-weight: 400;
    font-size: 50px;
    line-height: 1;
  }
  .brand__sub {
    font-weight: 400;
    font-size: 26px;
    letter-spacing: 0.55em;
    margin-top: 10px;
    padding-left: 0.55em;
  }

  .card--front .brand { position: absolute; top: 110px; left: 0; right: 0; }
  .tagline {
    position: absolute;
    left: 0; right: 0; top: 290px;
    text-align: center;
    font-weight: 300;
    font-size: 22px;
    letter-spacing: 0.04em;
  }

  .card--back .brand {
    position: absolute; top: 40px; left: 44px;
    align-items: flex-start;
  }
  .card--back .brand__name { font-size: 36px; }
  .card--back .brand__sub { font-size: 19px; margin-top: 8px; padding-left: 0; }

  .person { position: absolute; left: 46px; top: 158px; }
  .person__name {
    font-family: "Libre Baskerville", serif;
    font-size: 27px;
    line-height: 1.25;
    margin-bottom: 6px;
  }
  .person__role { font-size: 14px; line-height: 1.5; }

  .contact { position: absolute; left: 46px; top: 278px; list-style: none; }
  .contact__item {
    display: flex; align-items: center; gap: 12px;
    font-size: 16px; color: var(--ink); font-weight: 400;
    line-height: 26px;
    margin-bottom: 6px;
  }
  .contact__item:last-child { margin-bottom: 0; }
  .contact__icon { width: 26px; height: 26px; flex: none; }

  .word-cloud {
    position: absolute; right: 40px; top: 50px;
    width: 290px; height: 260px;
    border-radius: 12px;
    background: linear-gradient(135deg, var(--teal-soft), var(--coral-soft) 50%, var(--teal-soft));
  }
</style>
</head>
<body>

  <section class="card card--front">
    <div class="brand">
      <div class="brand__row">
        <span class="brand__dot"></span>
        <span class="brand__name">Bright Path</span>
      </div>
      <span class="brand__sub">COACHING</span>
    </div>
    <p class="tagline">True Happiness Comes From Within</p>
  </section>

  <section class="card card--back">
    <div class="brand">
      <div class="brand__row">
        <span class="brand__dot"></span>
        <span class="brand__name">Bright Path</span>
      </div>
      <span class="brand__sub">COACHING</span>
    </div>

    <div class="person">
      <h1 class="person__name">Mara Ellison</h1>
      <p class="person__role">Certified Professional Life Coach</p>
      <p class="person__role">Health &amp; Wellness Coach</p>
      <p class="person__role">Advanced Healing Path Method Specialist</p>
    </div>

    <ul class="contact">
      <li class="contact__item">
        <svg class="contact__icon" viewBox="0 0 26 26" aria-hidden="true">
          <circle cx="13" cy="13" r="13" fill="var(--teal)"/>
          <path d="M9 7.5c.8-.5 1.6-.3 2 .5l1 2c.3.6.1 1.2-.4 1.6l-.7.5c.6 1.4 1.6 2.4 3 3l.5-.7c.4-.5 1-.7 1.6-.4l2 1c.8.4 1 1.2.5 2-.9 1.4-2.4 2-4 1.3-3-1.3-5.300-3.6-6.6-6.6-.7-1.6-.1-3.1 1.1-4.2z" fill="#fff"/>
        </svg>
        (555) 014-2290
      </li>
      <li class="contact__item">
        <svg class="contact__icon" viewBox="0 0 26 26" aria-hidden="true">
          <circle cx="13" cy="13" r="13" fill="var(--teal)"/>
          <rect x="6.5" y="8.5" width="13" height="9" rx="1" fill="none" stroke="#fff" stroke-width="1.5"/>
          <path d="M6.5 9l6.5 5 6.5-5" fill="none" stroke="#fff" stroke-width="1.5"/>
        </svg>
        mara@brightpathcoaching.com
      </li>
      <li class="contact__item">
        <svg class="contact__icon" viewBox="0 0 26 26" aria-hidden="true">
          <circle cx="13" cy="13" r="13" fill="var(--teal)"/>
          <g fill="none" stroke="#fff" stroke-width="1.3">
            <circle cx="13" cy="13" r="6.5"/>
            <ellipse cx="13" cy="13" rx="3" ry="6.5"/>
            <path d="M6.5 13h13M7.5 9.8h11M7.5 16.2h11"/>
          </g>
        </svg>
        www.brightpathcoaching.com
      </li>
    </ul>

    <div class="word-cloud" role="img" aria-label="Word cloud illustration of coaching themes such as hope, joy, love, peace and clarity, with the phrase feel better, live well"></div>
  </section>

</body>
</html>
```